Chart Your Own Harbor Promotional Flyer

I Need a one page, one-sided 8.5 x 11 editable promotional flyer that POPS!, designed in photoshop

[TITLE]Chart Your Own Harbor: 3 BRIGHT Steps to Lift Your Practice Today!

[CONTENT for the Flyer:]

At this content-rich event you will learn how to:
• Get out of feast and famine mode and into six, multi-six and/or seven figure-income mode
• Leapfrog your competition and become the obvious choice in your market
• Have your business aligned with who you are and what you want
• Enjoy your business far more than you imagined possible.
• Have more fun and time to yourself
• Live free and unbound!

Accolades
“Delphine helped us increase our six figure income by 41%...I feel reborn!” Marlene & Otis Pruitt, Vienna, VA

“…Delphine is a joy to listen to - compelling, smart, provocative…” – Dwight Fennimore, Charlotte, North Carolina

“Delphine helped me increase my business by 66%...without me spending more time, money, or making cold calls! …I am in the zone!” Tess Calloway, Baltimore, MD
“Delphine is an energetic and dynamic speaker…content-rich…holds your attention to the very end!” Hal Brisbee, Frmr Pres., Kemper & Vail, MD, MD, D.C., PA, DE, NJ
“Delphine is the real estate whisperer!” Lou Tremaine, Washington D.C.

“Delphine was prepared, funny, informative and made a connection with each of our agents…Fabulous!…even my admins were PUMPED!!! – Paul Devereux, New York

About Delphine:
Delphine is a highly regarded business development speaker & coach who knows how to pump up an audience and have them making more money, in less time, AND having more fun doing it! What’s not to love?! Consistently rated as an exceptional speaker and conference favorite! Among her work: Magnet Method: How to Draw Your Dream Buyers Time After Time!, Client Pipelines Without Fuss, The Costliest Outreach Blunders Real Estate Agents Commit and How to Sidestep Them, Hard Seasons Forge Hard Sellers, Fuel for the Spirit for Real Estate Agents.

[Also need a section for:]
Date: December 9, 2015, Time: 9:00 Am - 12:00 Noon, Place: Silver Maple Conference, Ashford Hollow, PA

Target Market(s)

Real Estate Agents

Industry/Entity Type

Real Estate Agent

Font styles to use
Sans Serif

Colors
0655a3
f37122

Requirements
Must have
• the top tier prop mentor logo
Nice to have
• chart your own harbor logo; lots of POP! :-) ; open to other colors, accent colors.

```html
<!DOCTYPE html>
<html lang="en">
<head>
<meta charset="utf-8">
<title>Chart Your Own Harbor – Event Flyer</title>
<link href="https://fonts.googleapis.com/css2?family=Oswald:wght@500;600&family=Open+Sans:wght@400;600;700&family=Source+Sans+3:wght@300;400;600&display=swap" rel="stylesheet">
<style>
  :root{
    --navy:#2a3890;
    --blue:#0655a3;
    --blue-deep:#0b3f78;
    --blue-light:#2a7cc7;
    --orange:#f37122;
    --gold:#f5a623;
    --ribbon-dark:#243a7a;
    --ribbon-fold:#7a1c10;
    --ink:#222;
    --paper:#ffffff;
  }
  *{margin:0;padding:0;box-sizing:border-box}
  html,body{width:965px;height:1200px;overflow:hidden;background:#e9e9e9}
  .flyer{position:relative;width:965px;height:1200px;overflow:hidden;
    background:linear-gradient(180deg,#fff 0%,#f7f7f7 60%,#efefef 100%);
    font-family:"Source Sans 3",sans-serif;color:var(--ink)}
  .abs{position:absolute}
  .headline{top:48px;left:0;width:965px;text-align:center;font-family:"Oswald",sans-serif;
    font-weight:600;font-size:72px;letter-spacing:1px;color:var(--navy);line-height:1}
  .subhead{top:143px;left:0;width:965px;text-align:center;font-family:"Open Sans",sans-serif;
    font-weight:700;font-size:33px;color:var(--gold);letter-spacing:.3px}
  .band{top:0;left:0}
  .time-box{left:213px;top:222px;width:363px;height:50px;background:var(--ribbon-dark);
    border-radius:8px 8px 0 0;color:#fff;font-family:"Oswald",sans-serif;font-weight:600;
    font-size:36px;text-align:center;line-height:50px}
  .time-box small{font-size:24px}
  .date-box{left:215px;top:271px;width:359px;height:65px;border-radius:0 0 10px 10px;
    background:linear-gradient(180deg,#f59a3a,var(--orange));color:#fff;text-align:center;
    font-family:"Oswald",sans-serif;font-weight:600;font-size:40px;line-height:65px;
    letter-spacing:1px;text-shadow:0 2px 2px rgba(0,0,0,.35);box-shadow:0 3px 5px rgba(0,0,0,.3)}
  .learn-title{left:47px;top:352px;font-family:"Oswald",sans-serif;font-weight:500;
    font-size:25px;color:var(--gold)}
  .learn-list{left:47px;top:402px;width:470px;list-style:none;color:#fff;font-size:16px;
    font-weight:300;line-height:18px}
  .learn-list li{position:relative;padding-left:22px;margin-bottom:5px}
  .learn-list li::before{content:"";position:absolute;left:0;top:3px;width:13px;height:13px;
    border-radius:50%;background:radial-gradient(circle at 40% 35%,#ffe27a,var(--gold) 70%)}
  .tagline{left:600px;top:285px;width:335px;text-align:center;font-family:"Open Sans",sans-serif;
    font-weight:700;font-size:28px;line-height:36px;color:var(--gold)}
  .place{left:595px;top:410px;width:345px;text-align:center;font-family:"Oswald",sans-serif;
    font-weight:600;font-size:26px;line-height:44px;color:#fff}
  .portrait{left:744px;top:536px;width:221px;height:219px;
    background:linear-gradient(180deg,#f3f3f3 0%,#e8c9a6 35%,#d9b48a 55%,#2b2b2b 80%,#1d1d1d 100%)}
  .brand-left{left:69px;top:630px;width:320px;height:100px;display:flex;align-items:center;gap:12px}
  .brand-left .dot{width:22px;height:22px;border-radius:50%;background:var(--orange)}
  .brand-left span{font-family:"Open Sans",sans-serif;font-weight:600;font-size:30px;color:var(--navy);line-height:1.05}
  .brand-mid{left:470px;top:585px;width:280px;text-align:center}
  .brand-mid .name{font-family:"Open Sans",sans-serif;font-weight:700;font-size:26px;color:var(--orange)}
  .brand-mid .mark{font-family:"Open Sans",sans-serif;font-weight:700;font-size:30px;
    line-height:34px;color:var(--orange);margin-top:6px;text-transform:uppercase}
  .rule{left:0;top:755px;width:965px;height:9px;
    background:linear-gradient(90deg,var(--gold),#f7c64a 40%,var(--orange) 100%)}
  .col-title{font-family:"Open Sans",sans-serif;font-weight:400;font-size:27px;color:var(--navy)}
  .about{left:49px;top:786px;width:274px}
  .about p{margin-top:14px;font-size:14.6px;line-height:21.8px;text-align:justify;color:#222}
  .divider{left:363px;top:792px;width:1px;height:370px;background:#d6d6d6}
  .accolades{left:404px;top:786px;width:525px}
  .quote{font-size:13.5px;line-height:18px;color:#222;margin-top:16px}
  .who{font-family:"Open Sans",sans-serif;font-weight:700;font-size:12.5px;margin-top:8px}
  .sep{height:1px;background:var(--orange);margin-top:12px;opacity:.8}
  .quote.tight{margin-top:6px}
</style>
</head>
<body>
<main class="flyer">
  <h1 class="abs headline">CHART YOUR OWN HARBOR</h1>
  <p class="abs subhead">3 BRIGHT STEPS TO LIFT YOUR PRACTICE TODAY!</p>

  <svg class="abs band" width="965" height="760" viewBox="0 0 965 760" aria-hidden="true">
    <defs>
      <linearGradient id="bandFill" x1="0" y1="0" x2="1" y2="0">
        <stop offset="0" stop-color="#2a7cc7"/>
        <stop offset=".45" stop-color="#0655a3"/>
        <stop offset="1" stop-color="#0b3f78"/>
      </linearGradient>
    </defs>
    <polygon fill="url(#bandFill)"
      points="0,250 141,250 177,286 611,286 643,250 965,250 965,555 458,555 426,590 0,590"/>
    <polygon fill="#7a1c10" points="189,272 213,258 213,290"/>
    <polygon fill="#7a1c10" points="600,272 576,258 576,290"/>
  </svg>

  <div class="abs time-box">9:00 <small>AM</small> - 12:00 Noon</div>
  <div class="abs date-box">DECEMBER 9, 2015</div>

  <h2 class="abs learn-title">At this content-rich event you will learn how to:</h2>
  <ul class="abs learn-list">
    <li>Get out of feast and famine mode and into six, multi-six and/or seven figure-income mode</li>
    <li>Leapfrog your competition and become the obvious choice in your market</li>
    <li>Have your business aligned with who you are and what you want</li>
    <li>Enjoy your business far more than you imagined possible.</li>
    <li>Have more fun and time to yourself</li>
    <li>Live free and unbound!</li>
  </ul>

  <p class="abs tagline">“America’s Top Tier Property Mentor”™</p>
  <p class="abs place">Place:<br>Silver Maple Conference,<br>Ashford Hollow, PA</p>

  <div class="abs portrait" role="img" aria-label="Portrait photo of Delphine Ashcombe, smiling, in a dark blazer"></div>

  <div class="abs brand-left"><div class="dot"></div><span>Chart Your Own Harbor</span></div>

  <div class="abs brand-mid">
    <div class="name">Delphine Ashcombe</div>
    <div class="mark">Top Tier<br>Prop Mentor</div>
  </div>

  <div class="abs rule"></div>

  <section class="abs about">
    <h2 class="col-title">About Delphine</h2>
    <p>Delphine is a highly regarded business development speaker &amp; coach who knows how to pump up an audience and have them making more money, in less time, AND having more fun doing it! What’s not to love?! Consistently rated as an exceptional speaker and conference favorite! Among her work: Magnet Method: How to Draw Your Dream Buyers Time After Time!, Client Pipelines Without Fuss, The Costliest Outreach Blunders Real Estate Agents Commit and How to Sidestep Them, Hard Seasons Forge Hard Sellers, Fuel for the Spirit for Real Estate Agents.</p>
  </section>

  <div class="abs divider"></div>

  <section class="abs accolades">
    <h2 class="col-title">Accolades</h2>
    <p class="quote">“Delphine helped us increase our six figure income by 41%...I feel reborn!”</p>
    <p class="who">Marlene &amp; Otis Pruitt, Vienna, VA</p>
    <div class="sep"></div>
    <p class="quote">“Delphine is a joy to listen to - compelling, smart, provocative”</p>
    <p class="who">Dwight Fennimore, Charlotte, North Carolina</p>
    <div class="sep"></div>
    <p class="quote">“Delphine helped me increase my business by 66%...without me spending more time, money, or making cold calls! ...I am in the zone!” Tess Calloway, Baltimore, MD</p>
    <p class="quote tight">“Delphine is an energetic and dynamic speaker...content-rich...holds your attention to the very end!” Hal Brisbee, Frmr Pres., Kemper &amp; Vail, MD, MD, D.C., PA, DE, NJ</p>
    <p class="quote tight">“Delphine is the real estate whisperer!”</p>
    <p class="who">Lou Tremaine, Washington D.C.</p>
    <div class="sep"></div>
    <p class="quote">“Delphine was prepared, funny, informative and made a connection with each of our agents...Fabulous!...even my admins were PUMPED!!!</p>
    <p class="who">Paul Devereux, New York</p>
  </section>
</main>
</body>
</html>
```